Stationary pack for BrightNest

BrightNest is a recently establish Solar brokerage company based in Australia. We have a number of sales staff who provide advice and guidance to both residential and commercial customers regarding solar systems (solar hot water and solar panels.)

In addition to our brokerage services we are also developing software for the solar industry, which will be used to automate the solar system install process. This system will be used by other companies in the solar industry including installers, wholesalers and government departments.

We are after a stationary pack that consists of the following: Business cards, compliments slip and letter head.

The EPS, AI, PNG etc files for the logo are attached.

For the business card:
The name and logo of the company need to be clearly visible. On the back of the business cards, we would like the logo. I am happy for you to split the image part of the logo from the text if you think it would look better a different way.

I would like the business cards to be easily readable with the following information on the front:
Name
(Please leave room for titles for the future – eg Sales Advisor.)
Mobile
Office
Email
Address
ABN

Letter heads:
I would prefer the address to be at the top

Compliments slips:
Only need to be one sided

Target Market(s)

BrightNest provides services to both residential and commercial customers. Our customers will be environmentally conscious.

Industry/Entity Type

Residential

Requirements
Must have
• Business cards must have the logo on the back.

```html
<!DOCTYPE html>
<html lang="en">
<head>
<meta charset="utf-8">
<title>BrightNest Stationery Pack</title>
<link href="https://fonts.googleapis.com/css2?family=Nunito:wght@400;600;800&display=swap" rel="stylesheet">
<style>
  :root {
    --sun-yellow: #fbd12e;
    --sun-orange: #f6a81c;
    --deep-orange: #f29a13;
    --leaf-green: #6cb535;
    --lime-green: #a6cf3a;
    --brand-green: #3f9a3a;
    --paper-cream: #fdf8ec;
    --grid-tint: #dfeac8;
    --card-edge: #8a8a8a;
    --text-green: #4e9a3a;
    --white: #ffffff;
  }
  * { box-sizing: border-box; margin: 0; padding: 0; }
  html, body { width: 1200px; height: 900px; overflow: hidden; background: var(--white); }
  body { position: relative; font-family: "Nunito", Arial, sans-serif; }

  .brand { position: absolute; display: flex; align-items: center; gap: 6px; white-space: nowrap; }
  .brand-dot { border-radius: 50%; background: var(--brand-green); flex: none; }
  .brand-name { font-weight: 800; color: var(--brand-green); letter-spacing: -0.3px; line-height: 1; }

  .panel-grid {
    position: absolute;
    background: linear-gradient(175deg, rgba(223,234,200,0) 0%, rgba(223,234,200,0.55) 45%, rgba(200,222,160,0.75) 100%);
  }

  /* Letterhead */
  .letterhead {
    position: absolute; left: 30px; top: 4px; width: 684px; height: 886px;
    background: var(--paper-cream); overflow: hidden;
  }
  .letterhead-header { position: absolute; left: 0; top: 0; width: 684px; height: 240px; }
  .letterhead .brand { left: 14px; top: 72px; gap: 5px; }
  .letterhead .brand-dot { width: 15px; height: 15px; }
  .letterhead .brand-name { font-size: 20px; }
  .letterhead-divider {
    position: absolute; left: 166px; top: 30px; width: 1px; height: 180px;
    background: rgba(255,255,255,0.8);
  }
  .letterhead-contact { position: absolute; left: 176px; top: 34px; color: var(--white); }
  .letterhead-contact .person-name { font-size: 13px; font-weight: 600; }
  .letterhead-contact .person-title { font-size: 10px; margin-top: 2px; }
  .letterhead-contact .details { margin-top: 26px; font-size: 8px; line-height: 11px; }
  .letterhead .panel-grid { left: 0; top: 600px; width: 684px; height: 286px; }

  /* Business card back */
  .card-back {
    position: absolute; left: 768px; top: 96px; width: 394px; height: 164px;
    border: 1px solid var(--card-edge);
    background: radial-gradient(ellipse at center, var(--sun-yellow) 0%, var(--sun-orange) 70%, var(--deep-orange) 100%);
  }
  .card-back .brand { left: 50%; top: 50%; transform: translate(-50%, -50%); }
  .card-back .brand-dot { width: 16px; height: 16px; }
  .card-back .brand-name { font-size: 22px; }

  /* Business card front */
  .card-front {
    position: absolute; left: 768px; top: 296px; width: 394px; height: 164px;
    border: 1px solid var(--card-edge); background: var(--white); overflow: hidden;
  }
  .card-front .brand { right: 14px; top: 14px; }
  .card-front .brand-dot { width: 12px; height: 12px; }
  .card-front .brand-name { font-size: 14px; }
  .card-front-contact { position: absolute; left: 10px; top: 60px; color: var(--text-green); }
  .card-front-contact .person-name { font-size: 12px; font-weight: 600; }
  .card-front-contact .person-title { font-size: 9px; margin-top: 1px; }
  .card-front-contact .details { margin-top: 14px; font-size: 7px; line-height: 9px; }
  .card-front .panel-grid { left: 120px; top: 70px; width: 274px; height: 94px; }

  /* Compliments slip */
  .comp-slip {
    position: absolute; left: 640px; top: 494px; width: 556px; height: 252px;
    background: linear-gradient(90deg, var(--sun-orange), var(--sun-yellow) 50%, var(--sun-orange));
    padding: 12px;
  }
  .comp-slip-inner {
    position: relative; width: 100%; height: 100%;
    background: var(--paper-cream); border-radius: 12px; overflow: hidden;
  }
  .comp-slip .brand { left: 14px; top: 26px; }
  .comp-slip .brand-dot { width: 14px; height: 14px; }
  .comp-slip .brand-name { font-size: 18px; }
  .comp-slip .panel-grid { left: 100px; top: 60px; width: 432px; height: 168px; }
</style>
</head>
<body>

  <section class="letterhead">
    <svg class="letterhead-header" viewBox="0 0 684 240" aria-hidden="true">
      <defs>
        <linearGradient id="sunBand" x1="0" y1="0" x2="1" y2="0">
          <stop offset="0" stop-color="#f6a81c"/>
          <stop offset="0.6" stop-color="#fbd12e"/>
          <stop offset="1" stop-color="#fde37a"/>
        </linearGradient>
        <linearGradient id="leafBand" x1="0" y1="0" x2="1" y2="0">
          <stop offset="0" stop-color="#5aa832"/>
          <stop offset="0.6" stop-color="#8cc63a"/>
          <stop offset="1" stop-color="#c6de5a"/>
        </linearGradient>
      </defs>
      <path d="M0 0 H684 V12 C500 70 280 130 0 170 Z" fill="url(#sunBand)"/>
      <path d="M0 170 C280 130 500 70 684 12 V26 C490 90 280 160 0 226 Z" fill="url(#leafBand)"/>
      <path d="M0 196 C260 150 480 90 684 24" stroke="#d9ea7a" stroke-width="3" fill="none" opacity="0.7"/>
    </svg>
    <div class="brand"><span class="brand-dot"></span><span class="brand-name">BrightNest</span></div>
    <div class="letterhead-divider"></div>
    <div class="letterhead-contact">
      <p class="person-name">Name</p>
      <p class="person-title">Sales Advisor</p>
      <p class="details">Mobile<br>Office<br>Email<br>Address<br>ABN</p>
    </div>
    <div class="panel-grid" role="img" aria-label="Faint solar panel grid decoration"></div>
  </section>

  <section class="card-back">
    <div class="brand"><span class="brand-dot"></span><span class="brand-name">BrightNest</span></div>
  </section>

  <section class="card-front">
    <div class="panel-grid" role="img" aria-label="Faint solar panel grid decoration"></div>
    <div class="brand"><span class="brand-dot"></span><span class="brand-name">BrightNest</span></div>
    <div class="card-front-contact">
      <p class="person-name">Name</p>
      <p class="person-title">Sales Advisor</p>
      <p class="details">Mobile<br>Office<br>Email<br>Address<br>ABN</p>
    </div>
  </section>

  <section class="comp-slip">
    <div class="comp-slip-inner">
      <div class="panel-grid" role="img" aria-label="Faint solar panel grid decoration"></div>
      <div class="brand"><span class="brand-dot"></span><span class="brand-name">BrightNest</span></div>
    </div>
  </section>

</body>
</html>
```